Business Card Design Project (Beer industry)

I am seeking a redesign of my business card. I am looking for something that will really stand out in both texture and feel. Something more on the modern side then traditional. Nothing die cut shaped like a beer mug please.

The card is used mostly for other industry professionals, as well as bar and restaurant owners. My title is Strategy & Acquisitions. If you would like to somehow incorporate that theme, that may work.

My business is craft and imported beer. Nothing fizzy and yellow, so my products are more on the upscale side.
Updates

I was able to update my logo in .ai and .tif format. I hope that helps. 

Thank you all for your creative ideas. I have uploaded my current business card in pdf format, as well as our logo in .eps file format. We are excited about the submissions so far and want to thank you all again.

PS Please do not include fax number in future submissions, as we are looking for something more creative and a fax says 1999 and not 2015, which is the message we are going for, without being futuristic. 

Thank you all once again for all of your submissions. If we would consider a two sided card, we would like the opposite side not to be the same as the front. The styles we have seen so far, it appears the front and back are too similar. Again, a two sided card is not required. Thank you and we look forward to pushing the boundaries of your creativity. Cheers

Target Market(s)

My card would mostly go to bar and restaurant operators as well as other beer industry professionals

Industry/Entity Type

Restaurant

Requirements
Nice to have
• Two sided would be considered, although not required
Should not have
• Anything die cut shaped like a beer mug.

```html
<!DOCTYPE html>
<html lang="en">
<head>
<meta charset="utf-8">
<title>Halden Brew – Business Card</title>
<link rel="stylesheet" href="https://fonts.googleapis.com/css2?family=Open+Sans:wght@400;600;700&family=Crimson+Text:ital@1&display=swap">
<style>
  :root {
    --backdrop: #2a2a2a;
    --card: #f5f5f4;
    --ink: #1b1b1b;
    --navy: #2a4a86;
    --ribbon: #a8201f;
    --ribbon-dark: #7a1514;
    --paper-text: #ffffff;
  }
  html, body {
    margin: 0;
    width: 1200px;
    height: 900px;
    overflow: hidden;
    background: var(--backdrop);
  }
  .card {
    position: absolute;
    left: 100px;
    top: 164px;
    width: 1000px;
    height: 571px;
    background: var(--card);
    box-shadow: 0 10px 30px rgba(0,0,0,.45);
    font-family: "Open Sans", Arial, sans-serif;
    color: var(--ink);
  }
  .brand {
    position: absolute;
    left: 60px;
    top: 170px;
    width: 400px;
    text-align: center;
  }
  .brand-mark {
    display: flex;
    align-items: center;
    justify-content: center;
    gap: 16px;
  }
  .brand-dot {
    width: 46px;
    height: 46px;
    border-radius: 50%;
    background: var(--navy);
  }
  .brand-name {
    font-weight: 700;
    font-size: 48px;
    letter-spacing: 1px;
    color: var(--ribbon);
  }
  .brand-tagline {
    margin-top: 22px;
    font-family: "Crimson Text", Georgia, serif;
    font-style: italic;
    font-size: 22px;
    color: #333;
  }
  .name-ribbon {
    position: absolute;
    left: 460px;
    top: 140px;
    width: 540px;
    height: 110px;
  }
  .name-block {
    position: absolute;
    left: 560px;
    top: 152px;
    color: var(--paper-text);
  }
  .person-name {
    font-weight: 700;
    font-size: 38px;
    letter-spacing: 1px;
    line-height: 1.1;
  }
  .person-title {
    font-size: 24px;
    letter-spacing: 1px;
  }
  .contacts {
    position: absolute;
    left: 560px;
    top: 290px;
    font-size: 30px;
    font-weight: 600;
    line-height: 36px;
  }
  .contact-row { display: flex; align-items: baseline; }
  .contact-label {
    width: 32px;
    font-size: 18px;
    font-weight: 400;
    color: var(--navy);
  }
  .address {
    position: absolute;
    left: 520px;
    top: 410px;
    font-size: 28px;
    font-weight: 600;
    line-height: 36px;
  }
  .website {
    position: absolute;
    left: 520px;
    top: 505px;
    font-size: 28px;
    font-weight: 600;
  }
  .website .domain { color: var(--navy); }
</style>
</head>
<body>
  <div class="card">
    <div class="brand">
      <div class="brand-mark">
        <span class="brand-dot"></span>
        <span class="brand-name">HALDEN BREW</span>
      </div>
      <div class="brand-tagline">Premier Craft &amp; Import Beer Distributor</div>
    </div>

    <svg class="name-ribbon" viewBox="0 0 540 110" aria-hidden="true">
      <polygon points="0,40 70,40 70,110 30,110 45,75" fill="var(--ribbon-dark)"/>
      <polygon points="40,0 540,0 540,110 40,110" fill="var(--ribbon)"/>
    </svg>
    <div class="name-block">
      <div class="person-name">DAN KELLER</div>
      <div class="person-title">SALES MANAGER</div>
    </div>

    <div class="contacts">
      <div class="contact-row"><span class="contact-label">t</span>(555) 214-7300</div>
      <div class="contact-row"><span class="contact-label">m</span>(555) 639-1847</div>
      <div class="contact-row"><span class="contact-label">e</span>dkeller@haldenbrew.com</div>
    </div>

    <div class="address">
      <div>42 Harbor Street</div>
      <div>Eastport, NY 10999</div>
    </div>

    <div class="website">www.<span class="domain">haldenbrew</span>.com</div>
  </div>
</body>
</html>
```